retro inspired postcard/flyer design project

Task Description
We are a concept bar in St Kilda (Australia). The bar is themed as a New York style loft apartment and has a retro/60's theme to it- we also use Benny Corrado style pop art in a lot of our design elements. Please check out our website for direction (www.velvetloungeroom.com.au)

We need a flyer/postcard designed as a promotion to give out to local corporate type businesses to Promote our Friday night after work free drinks deal

We need the flyer/postcard to be postcard size (approx A6) of any orientation and needs to be double sided.

We need the style of the flyer to give the impression that it is a postcard

I have attached the previous postcard that we used for promoting to a hospitality market- This flyer/postcard is a little too casula for the corporate market so we need a new one for these people. All the information needs to be the same as this one except the name of the night is 'GLITTERING GOLDEN HOURS' not 'Cheap Tab Thursdays' as we are promoting to more of a corporate market.. Saying all that we are a bar so the flyer/postcard still needs to have a fun element

I am happy to pay up to $20 for a stock image if this is needed for the final design that we choose...

Target Market(s)

Young professionals and corporate businesses in the St Kilda area- age group 25-40

Industry/Entity Type

Hospitality

Requirements
Must have
• Must look like a postcard
Must have all the information as shown in the attachement with the exception of the name of the night which needs to be 'Glittering Golden Hour's'

```html
<!DOCTYPE html>
<html lang="en">
<head>
<meta charset="utf-8">
<title>Velvet Lounge Room – Glittering Golden Hour's Postcard</title>
<link rel="stylesheet" href="https://fonts.googleapis.com/css2?family=Open+Sans:wght@300;400;600;700;800&family=Architects+Daughter&display=swap">
<style>
  :root {
    --backdrop-deep: #020816;
    --backdrop-blue: #0d2a66;
    --card-shadow: rgba(0,0,0,0.55);
    --promo-red: #e3262e;
    --ink-dark: #1f1f1f;
    --ink-grey: #4a4a4a;
    --paper-light: #f1e6c8;
    --paper-mid: #e4d2a8;
    --paper-edge: #cfb682;
    --photo-grey: #d6d6d6;
    --photo-red: #8f1e22;
    --photo-gold: #c9a62c;
    --white: #ffffff;
    --line-ink: #3a3a3a;
  }
  * { box-sizing: border-box; margin: 0; padding: 0; }
  html, body { width: 817px; height: 1200px; overflow: hidden; }
  body {
    position: relative;
    font-family: "Open Sans", Arial, sans-serif;
    background: radial-gradient(ellipse at 40% 45%, var(--backdrop-blue) 0%, #081a44 45%, var(--backdrop-deep) 100%);
  }
  .postcard {
    position: absolute;
    left: 88px;
    width: 636px;
    height: 452px;
    overflow: hidden;
    box-shadow: 0 4px 14px var(--card-shadow);
  }
  .postcard--front { top: 111px; }
  .postcard--back {
    top: 653px;
    background: radial-gradient(ellipse at 35% 40%, var(--paper-light) 0%, var(--paper-mid) 65%, var(--paper-edge) 100%);
  }

  /* front */
  .front-photo {
    position: absolute; inset: 0;
    background: linear-gradient(165deg, var(--photo-grey) 0%, #bdbdbd 22%, var(--photo-red) 42%, #a33a24 52%, var(--photo-gold) 66%, #d8d8d8 88%, #eeeeee 100%);
  }
  .brand-name {
    position: absolute;
    font-weight: 800;
    letter-spacing: 0.5px;
    white-space: nowrap;
  }
  .front-brand { left: 40px; top: 178px; font-size: 40px; color: var(--white); }
  .front-contact {
    position: absolute; left: 22px; top: 413px;
    font-size: 15px; font-weight: 700; color: var(--ink-dark);
    display: flex; gap: 52px;
  }

  .promo { position: absolute; line-height: 1; }
  .promo-label {
    display: inline-block;
    background: var(--promo-red); color: var(--white);
    font-weight: 700; padding: 1px 5px; white-space: nowrap;
  }
  .promo-free { color: var(--promo-red); font-weight: 800; letter-spacing: -1px; }
  .promo-drink { color: var(--ink-grey); font-weight: 400; letter-spacing: -1px; }

  .front-promo { right: 16px; top: 330px; text-align: right; }
  .front-promo .promo-label { font-size: 12.5px; }
  .front-promo .promo-free { font-size: 50px; margin-top: -2px; }
  .front-promo .promo-drink { font-size: 48px; margin-top: -4px; }

  /* back */
  .back-brand { left: 30px; top: 70px; font-size: 30px; color: var(--ink-dark); }
  .back-promo { left: 48px; top: 199px; }
  .back-promo .promo-label { font-size: 13px; }
  .back-promo .promo-free { font-size: 52px; margin-top: -2px; }
  .drink-row { display: flex; align-items: flex-end; gap: 14px; margin-top: -4px; }
  .back-promo .promo-drink { font-size: 52px; }
  .drink-detail { font-size: 12px; color: var(--ink-grey); line-height: 1.15; padding-bottom: 5px; }
  .drink-detail strong { display: block; font-size: 15px; font-weight: 700; }

  .booking { position: absolute; left: 82px; top: 391px; font-size: 12px; color: var(--ink-dark); line-height: 1.3; }
  .booking strong { display: block; font-size: 14.5px; font-weight: 700; }

  .divider { position: absolute; left: 380px; top: 20px; width: 1.5px; height: 410px; background: var(--line-ink); }

  .stamp {
    position: absolute; left: 518px; top: 24px; width: 96px; height: 126px;
    background: var(--white); padding: 6px;
    box-shadow: 0 1px 3px rgba(0,0,0,0.3);
  }
  .stamp-art {
    width: 100%; height: 100%;
    background: linear-gradient(170deg, #f4f1ec 0%, #e9dfd6 55%, #d9624a 80%, #2d2a2a 100%);
    position: relative;
  }
  .stamp-title {
    position: absolute; left: 4px; top: 4px; right: 4px;
    font-size: 9px; font-weight: 700; color: var(--promo-red); line-height: 1.1;
  }
  .postmark { position: absolute; left: 408px; top: 62px; }

  .address { position: absolute; left: 404px; top: 306px; width: 200px; }
  .address-line {
    height: 36px; border-bottom: 1.5px solid var(--line-ink);
    font-family: "Architects Daughter", cursive;
    font-size: 15px; color: var(--ink-dark); letter-spacing: 1px;
    display: flex; align-items: flex-end; padding: 0 0 2px 12px;
  }
  .address-line:first-child { height: 0; }
</style>
</head>
<body>

  <section class="postcard postcard--front">
    <div class="front-photo" role="img" aria-label="Retro black and white photograph of three smiling women in yellow outfits holding a red pennant"></div>
    <div class="brand-name front-brand">Velvet Lounge Room</div>

    <div class="promo front-promo">
      <span class="promo-label">Glittering Golden Hour's</span>
      <div class="promo-free">FREE</div>
      <div class="promo-drink">DRINK</div>
    </div>

    <div class="front-contact">
      <span>Phone: 9000 41 57</span>
      <span>www.velvetloungeroom.com.au</span>
    </div>
  </section>

  <section class="postcard postcard--back">
    <div class="brand-name back-brand">Velvet Lounge Room</div>

    <div class="promo back-promo">
      <span class="promo-label">Glittering Golden Hour's</span>
      <div class="promo-free">FREE</div>
      <div class="drink-row">
        <div class="promo-drink">DRINK</div>
        <div class="drink-detail">Selected<strong>Beers, Spirits</strong><strong>Wine &amp; Bubbles</strong></div>
      </div>
    </div>

    <div class="booking">online booking<strong>www.velvetloungeroom.com.au</strong></div>

    <div class="divider"></div>

    <svg class="postmark" width="110" height="80" viewBox="0 0 110 80" aria-hidden="true">
      <g fill="none" stroke="#8a8275" stroke-width="1.2">
        <path d="M0 10 q14 -8 28 0 t28 0 t28 0 t28 0"/>
        <path d="M0 30 q14 -8 28 0 t28 0 t28 0 t28 0"/>
        <path d="M0 50 q14 -8 28 0 t28 0 t28 0 t28 0"/>
        <path d="M0 70 q14 -8 28 0 t28 0 t28 0 t28 0"/>
      </g>
    </svg>

    <div class="stamp">
      <div class="stamp-art" role="img" aria-label="Pop art pin-up illustration lying on vinyl records">
        <div class="stamp-title">Glittering Golden Hour's</div>
      </div>
    </div>

    <div class="address">
      <div class="address-line"></div>
      <div class="address-line">14 MARLOW ST</div>
      <div class="address-line">BAYVALE 3190</div>
    </div>
  </section>

</body>
</html>
```